St. Paddy’s Day Invitation

Invitation to text to people:
6th Annual St. Paddy’s Day Party
Where: The Kelterbrook’s
When: Saturday, March 25
Acoustic session by Taddeo Lindqvist from Mr. Pocketwatch
Fundraiser for Milo Ferreday ‘Open Harbor’ Fund

Target Market(s)

Adults only, all friends from our town, Moorestown, NJ

Colors
00AB8E
00BBA5
67D7C9
C6EFE9
E9F9F6
59FF00
82FF00
B8FF75
E3FFCB
F4FFEA

```html
<!DOCTYPE html>
<html lang="en">
<head>
<meta charset="utf-8">
<title>6th Annual St. Paddy’s Day Party</title>
<link rel="stylesheet" href="https://fonts.googleapis.com/css2?family=Cormorant+Garamond:wght@500;600;700&family=Yellowtail&display=swap">
<style>
  :root {
    --ink: #232323;
    --card: #f8f8f6;
    --frame: #ffffff;
    --hat-green: #1f7a52;
    --deep-green: #0f3d2c;
    --wood: #8a6a58;
    --wood-dark: #6e5245;
    --gold: #c99a2e;
  }
  * { margin: 0; padding: 0; box-sizing: border-box; }
  html, body { width: 960px; height: 1200px; overflow: hidden; }
  body { font-family: "Cormorant Garamond", Georgia, serif; color: var(--ink); }

  .invitation { position: relative; width: 960px; height: 1200px; overflow: hidden; }

  .backdrop-photo {
    position: absolute; inset: 0;
    background:
      radial-gradient(ellipse 200px 260px at 60px 1020px, rgba(201,154,46,.75), transparent 70%),
      radial-gradient(ellipse 260px 120px at 420px 1130px, rgba(201,154,46,.7), transparent 70%),
      radial-gradient(ellipse 120px 280px at 920px 740px, rgba(60,170,70,.6), transparent 70%),
      linear-gradient(180deg, var(--hat-green) 0%, var(--deep-green) 38%, var(--wood) 52%, var(--wood-dark) 100%);
  }

  .outer-frame {
    position: absolute; left: 140px; top: 176px; width: 684px; height: 854px;
    border: 1px solid var(--frame);
  }

  .card {
    position: absolute; left: 150px; top: 190px; width: 661px; height: 826px;
    background: var(--card);
    text-align: center;
  }
  .card > * { position: absolute; left: 0; right: 0; }

  .title {
    top: 102px; font-weight: 700; font-size: 37px; line-height: 42px;
    letter-spacing: 5px; text-transform: uppercase;
  }
  .label {
    font-weight: 700; font-size: 31px; letter-spacing: 1px; text-transform: uppercase;
  }
  .label--when { top: 266px; }
  .label--where { top: 386px; }
  .detail {
    font-weight: 700; font-size: 19px; letter-spacing: 3px; text-transform: uppercase;
  }
  .detail--date { top: 326px; }
  .detail--place { top: 446px; }
  .music {
    top: 545px; font-weight: 600; font-size: 15px; letter-spacing: .6px; text-transform: uppercase;
  }
  .fundraiser {
    top: 592px; font-weight: 600; font-size: 21px; line-height: 27px;
    letter-spacing: 2px; text-transform: uppercase;
  }
  .rule {
    top: 701px; left: 287px; right: auto; width: 87px; height: 1px; background: var(--ink);
  }
  .signoff {
    top: 740px; font-family: "Yellowtail", cursive; font-size: 27px;
  }
</style>
</head>
<body>
<main class="invitation">
  <div class="backdrop-photo" role="img" aria-label="Photo of a green leprechaun hat, shamrock-print fabric, gold clover coins and green bead necklaces on a wooden table"></div>
  <div class="outer-frame"></div>
  <section class="card">
    <h1 class="title">6th Annual<br>St. Paddy’s Day Party</h1>
    <h2 class="label label--when">When</h2>
    <p class="detail detail--date">Saturday, March 25</p>
    <h2 class="label label--where">Where</h2>
    <p class="detail detail--place">The Kelterbrook’s</p>
    <p class="music">Acoustic session by Taddeo Lindqvist from Mr. Pocketwatch</p>
    <p class="fundraiser">Fundraiser for Milo Ferreday<br>‘Open Harbor’ Fund</p>
    <div class="rule"></div>
    <p class="signoff">Hope to see you there!</p>
  </section>
</main>
</body>
</html>
```